Velmora Partners - website for real estate investment company

Create a bold, modern website that reflects Velmora’s success, professionalism, and credibility.
The design must stand out while maintaining a polished, corporate tone. (bold, but understated)
The client just created a new logo, and the website design must be in sync with the logo design. Information about the logo colors, fonts, and message are in the attached design brief.
Updates

Target Market(s)

b2b: banks, brokers, institutional partners, vendors, and property sellers.

Industry/Entity Type

real estate investment company

Number of Pages Required

1 page

Font styles to use
Sans Serif

Colors

Designer to choose colors to be used in the design.

Requirements
Must have
• 1. homepage design (psd) 2. a top banner image (psd) for a default inner page
Nice to have
• please see attached design brief
Should not have

```html
<!DOCTYPE html>
<html lang="en">
<head>
<meta charset="UTF-8">
<title>Velmora Partners</title>
<link href="https://fonts.googleapis.com/css2?family=Barlow:wght@400;500;600;700;800&display=swap" rel="stylesheet">
<style>
:root{
  --red:#d91f2b;
  --ink:#3a3a3a;
  --ink-soft:#555;
  --line:#dcdcdc;
  --panel:#f2f2f2;
  --white:#fff;
  --dark:#1c2027;
}
*{box-sizing:border-box;margin:0;padding:0}
html,body{width:1067px;height:1200px;overflow:hidden}
body{font-family:"Barlow",Arial,sans-serif;color:var(--ink);background:var(--white);position:relative}
.abs{position:absolute}

/* header */
.site-header{position:absolute;left:0;top:0;width:1067px;height:56px;background:var(--white);border-bottom:1px solid #e6e6e6}
.brand{position:absolute;left:134px;top:12px;display:flex;align-items:center;gap:6px;font-weight:800;font-size:29px;letter-spacing:.5px;color:var(--ink);line-height:1}
.brand-mark{width:10px;height:10px;background:var(--red)}
.main-nav{position:absolute;left:345px;top:22px;display:flex;gap:17px;font-size:9.6px;font-weight:500;letter-spacing:.4px;text-transform:uppercase;color:var(--ink)}
.main-nav .active{color:var(--red)}
.head-btn{position:absolute;top:14px;width:27px;height:27px;border:1px solid var(--ink);border-radius:2px;display:flex;align-items:center;justify-content:center}

/* hero */
.hero{position:absolute;left:0;top:56px;width:1067px;height:416px;background:linear-gradient(180deg,#2a2f38 0%,#3a3d44 45%,#2b2a2e 100%)}
.hero-glow{position:absolute;inset:0;background:radial-gradient(ellipse at 35% 35%,rgba(150,120,90,.25),transparent 60%)}
.hero-title{position:absolute;left:0;width:1067px;top:214px;text-align:center;font-weight:800;font-size:27px;letter-spacing:.5px;color:var(--red)}
.hero-text{position:absolute;left:278px;width:511px;top:256px;text-align:center;font-size:12px;line-height:15.5px;color:var(--white)}

/* stats */
.stat{position:absolute;top:528px;display:flex;align-items:center}
.stat-icon{width:53px;height:54px;background:#ececec;clip-path:polygon(0 0,100% 0,0 100%);position:absolute;left:0;top:0}
.stat-svg{position:absolute;left:12px;top:10px}
.stat-num{font-weight:800;font-size:26px;line-height:1;color:var(--red)}
.stat-label{font-size:14.5px;font-weight:500;color:var(--ink-soft);margin-top:3px;white-space:nowrap}

/* map + inquiry */
.map{position:absolute;left:0;top:634px;width:394px;height:344px;background:linear-gradient(135deg,#eef0f3,#e4e8ee 60%,#f1efea)}
.map-divider{position:absolute;left:394px;top:634px;width:5px;height:344px;background:#4a4a4a}
.inquiry{position:absolute;left:399px;top:634px;width:668px;height:344px;background:var(--panel)}
.inquiry-title{position:absolute;left:399px;width:562px;top:695px;text-align:center;font-size:25px;font-weight:700;letter-spacing:.5px;color:#474747}
.field-label{position:absolute;font-size:10px;color:var(--ink)}
.field{position:absolute;height:29px;background:var(--white);border:1px solid var(--line);display:flex;align-items:center;padding-left:9px}
.submit{position:absolute;left:646px;top:884px;width:69px;height:28px;background:#474747;color:var(--white);font-size:10px;font-weight:700;letter-spacing:.5px;display:flex;align-items:center;justify-content:center;border-radius:2px}

/* footer */
.footer{position:absolute;left:0;top:978px;width:1067px;height:188px;background:linear-gradient(180deg,#1d2129,#23262c)}
.footer-brand{position:absolute;left:134px;top:1042px;font-weight:800;font-size:52px;line-height:1;color:var(--white);letter-spacing:.5px}
.footer-head{position:absolute;top:1024px;font-size:14.5px;font-weight:700;letter-spacing:.5px;color:var(--red)}
.contact-row{position:absolute;left:477px;display:flex;align-items:center;gap:9px;font-size:10px;color:var(--white)}
.quick-link{position:absolute;font-size:10px;color:var(--white)}
.quick-link.active{color:var(--red)}

.bottom-bar{position:absolute;left:0;top:1166px;width:1067px;height:34px;background:var(--red)}
.copyright{position:absolute;left:134px;top:1176px;font-size:10px;color:var(--white)}
.social{position:absolute;top:1174px;width:17px;height:17px;border:1.5px solid var(--white);border-radius:50%}
.social.on{background:var(--white)}
</style>
</head>
<body>

<header class="site-header">
  <div class="brand"><span class="brand-mark"></span>VELMORA</div>
  <nav class="main-nav">
    <span class="active">Home</span>
    <span>Our Story</span>
    <span>Investment Strategy</span>
    <span>What Sets Us Apart</span>
    <span>Our Portfolio</span>
    <span>Contact Us</span>
  </nav>
  <div class="head-btn" style="left:873px">
    <svg width="10" height="8" viewBox="0 0 10 8"><rect width="10" height="8" rx="1" fill="#d91f2b"/><path d="M0.5 1 L5 4.5 L9.5 1" stroke="#fff" fill="none"/></svg>
  </div>
  <div class="head-btn" style="left:906px">
    <svg width="10" height="10" viewBox="0 0 24 24"><path fill="#d91f2b" d="M6.6 10.8a15 15 0 0 0 6.6 6.6l2.2-2.2a1 1 0 0 1 1-.25 11.4 11.4 0 0 0 3.6.6 1 1 0 0 1 1 1V20a1 1 0 0 1-1 1A17 17 0 0 1 3 4a1 1 0 0 1 1-1h3.5a1 1 0 0 1 1 1c0 1.25.2 2.45.6 3.6a1 1 0 0 1-.25 1z"/></svg>
  </div>
</header>

<section class="hero" role="img" aria-label="Evening aerial view of a downtown skyline with glass towers and a river">
  <div class="hero-glow"></div>
</section>
<h1 class="hero-title">EXPERIENCE – STRATEGY – VISION</h1>
<p class="hero-text">Velmora Partners is a vertically integrated real estate investment firm with a proven four-decade track record. We acquire, reposition, and operate high-performing assets across multiple sectors - always with a focus on exceptional, risk-adjusted returns.</p>

<div class="stat" style="left:151px">
  <div style="position:relative;width:57px;height:54px"><span class="stat-icon"></span>
    <svg class="stat-svg" width="30" height="34" viewBox="0 0 30 34" fill="none" stroke="#d91f2b" stroke-width="1.8"><circle cx="15" cy="9" r="6"/><path d="M3 33v-7a8 8 0 0 1 8-8h8a8 8 0 0 1 8 8v7z"/><path d="M12 18l3 5 3-5"/></svg>
  </div>
  <div><div class="stat-num">1989</div><div class="stat-label">Founded</div></div>
</div>
<div class="stat" style="left:329px">
  <div style="position:relative;width:70px;height:54px"><span class="stat-icon"></span>
    <svg class="stat-svg" width="38" height="36" viewBox="0 0 38 36" fill="none" stroke="#d91f2b" stroke-width="1.8"><rect x="4" y="10" width="30" height="25"/><rect x="14" y="1" width="10" height="9" fill="#555" stroke="#555"/><path d="M19 3v5M16.5 5.5h5" stroke="#fff"/><rect x="9" y="15" width="4" height="4"/><rect x="17" y="15" width="4" height="4"/><rect x="25" y="15" width="4" height="4"/><rect x="9" y="23" width="4" height="4"/><rect x="25" y="23" width="4" height="4"/><rect x="16" y="26" width="6" height="9" fill="#555" stroke="#555"/></svg>
  </div>
  <div><div class="stat-num">23,000+</div><div class="stat-label">Multifamily &amp; healthcare units</div></div>
</div>
<div class="stat" style="left:649px">
  <div style="position:relative;width:72px;height:54px"><span class="stat-icon"></span>
    <svg class="stat-svg" width="42" height="36" viewBox="0 0 42 36" fill="none" stroke="#d91f2b" stroke-width="1.8"><circle cx="22" cy="9" r="8" fill="#444" stroke="#444"/><text x="22" y="13" font-size="11" text-anchor="middle" fill="#fff" stroke="none" font-family="Barlow,sans-serif" font-weight="700">$</text><path d="M2 34l3-10h12l5 3h14l4-3-4 8H6"/></svg>
  </div>
  <div><div class="stat-num">$300+</div><div class="stat-label">Million invested in renovations</div></div>
</div>

<div class="map" role="img" aria-label="Street map showing the office location"></div>
<div class="map-divider"></div>
<section class="inquiry"></section>
<h2 class="inquiry-title">QUICK INQUIRY</h2>

<span class="field-label" style="left:438px;top:738px">Name</span>
<span class="field-label" style="left:606px;top:738px">Your Email</span>
<span class="field-label" style="left:772px;top:738px">Phone Number</span>
<div class="field" style="left:439px;top:754px;width:161px">
  <svg width="9" height="9" viewBox="0 0 10 10" fill="none" stroke="#d91f2b"><circle cx="5" cy="3" r="2.3"/><path d="M1 9.5a4 4 0 0 1 8 0z"/></svg>
</div>
<div class="field" style="left:606px;top:754px;width:161px">
  <svg width="10" height="8" viewBox="0 0 10 8" fill="none" stroke="#d91f2b"><rect x=".5" y=".5" width="9" height="7"/><path d="M.5 .5L5 4.5 9.5 .5"/></svg>
</div>
<div class="field" style="left:772px;top:754px;width:161px">
  <svg width="7" height="10" viewBox="0 0 7 10" fill="none" stroke="#d91f2b"><rect x=".5" y=".5" width="6" height="9" rx="1"/><path d="M3 8h1"/></svg>
</div>
<span class="field-label" style="left:439px;top:794px">Your Message</span>
<div class="field" style="left:439px;top:810px;width:494px;height:63px;align-items:flex-start;padding-top:9px">
  <svg width="9" height="9" viewBox="0 0 10 10" fill="none" stroke="#d91f2b"><path d="M.5 .5h9v6l-3 3h-6z"/></svg>
</div>
<div class="submit">SUBMIT</div>

<footer class="footer" role="img" aria-label="Dark city skyline background"></footer>
<div class="footer-brand">VELMORA</div>

<div class="footer-head" style="left:477px">CONATCT INFO</div>
<div class="contact-row" style="top:1058px">
  <svg width="11" height="13" viewBox="0 0 12 14"><path fill="#d91f2b" d="M6 0a5 5 0 0 1 5 5c0 4-5 9-5 9S1 9 1 5a5 5 0 0 1 5-5z"/><circle cx="6" cy="5" r="2" fill="#23262c"/></svg>
  <span>412 Harbor Ave, Lakeview, NJ 08730</span>
</div>
<div class="contact-row" style="top:1082px">
  <svg width="11" height="11" viewBox="0 0 24 24"><path fill="#d91f2b" d="M6.6 10.8a15 15 0 0 0 6.6 6.6l2.2-2.2a1 1 0 0 1 1-.25 11.4 11.4 0 0 0 3.6.6 1 1 0 0 1 1 1V20a1 1 0 0 1-1 1A17 17 0 0 1 3 4a1 1 0 0 1 1-1h3.5a1 1 0 0 1 1 1c0 1.25.2 2.45.6 3.6a1 1 0 0 1-.25 1z"/></svg>
  <span>(555) 014-2286</span>
</div>
<div class="contact-row" style="top:1104px">
  <svg width="11" height="8" viewBox="0 0 10 8"><rect width="10" height="8" fill="#d91f2b"/><path d="M0.5 1 L5 4.5 L9.5 1" stroke="#23262c" fill="none"/></svg>
  <span>info@velmora.com</span>
</div>

<div class="footer-head" style="left:710px">QUICK LINK</div>
<span class="quick-link active" style="left:710px;top:1056px">Home</span>
<span class="quick-link" style="left:710px;top:1075px">Our Story</span>
<span class="quick-link" style="left:710px;top:1094px">Investment Strategy</span>
<span class="quick-link" style="left:710px;top:1113px">What Sets Us Apart</span>
<span class="quick-link" style="left:847px;top:1056px">Our Portfolio</span>
<span class="quick-link" style="left:847px;top:1075px">Contact Us</span>
<span class="quick-link" style="left:847px;top:1094px">Trams &amp; Condition</span>
<span class="quick-link" style="left:847px;top:1113px">Privacy Policy</span>

<div class="bottom-bar"></div>
<div class="copyright">© 2025 VELMORA. All Right Reserved</div>
<span class="social" style="left:823px"></span>
<span class="social on" style="left:847px"></span>
<span class="social" style="left:872px"></span>
<span class="social" style="left:896px"></span>
<span class="social" style="left:920px"></span>

</body>
</html>
```